Illustrations for a Project Management Concept

we need illustrations for 5 project management principles that make up a holistic approach to project management, without all the BS. if we extract all the methodology, system, tool and mumbo-jumbo out of project management, we end up with some essential principles that are simple to understand and use. It's likely that people who use them will not be traditional Project Management types.

I've mocked up something that looks very corporate based on a template, but this has the wrong tone; the wrong feeling. I'd like something "funky" and colorful that conveys "Action" within "Simplicity".

the PPT file with the dark-blue background is the "corporate" consulting type mockup. the PPT with the white background shows an idea I had for breaking out each of the 5 principles (only one shown) to make it larger, with some text in a callout.

In the final deliverable, I need to be able to both show all 5 on one diagram, as well as slicing the image to display each principle separately. i do not have editing capabilities for vector image formats, only image formats

Reason: there are a number of designers who have only just accepted the invitation. I want to give everyone a chance to submit.

```html
<!DOCTYPE html>
<html lang="en">
<head>
<meta charset="utf-8">
<title>Achieve Outcomes – Project Principles</title>
<link rel="stylesheet" href="https://fonts.googleapis.com/css2?family=Jost:wght@700;800&display=swap">
<style>
  :root {
    --sky-deep: #1681c4;
    --sky-mid: #2f9ad6;
    --sky-light: #7ccbf0;
    --grid-line: rgba(255, 255, 255, 0.22);
    --hub-glow: rgba(160, 222, 250, 0.55);

    --value-light: #f6aa3a;
    --value-dark: #bd8a34;
    --value-rim: #f8bb4e;

    --models-light: #ee2a2c;
    --models-dark: #b7202c;
    --models-rim: #f2484a;

    --entropy-light: #3dbb70;
    --entropy-dark: #0b9143;
    --entropy-rim: #4cc77c;

    --teaming-light: #e8702a;
    --teaming-dark: #b45326;
    --teaming-rim: #ee8443;

    --core-light: #f7ea1e;
    --core-dark: #f0b31b;
    --core-rim: #fff4a6;

    --label-light: #ffffff;
    --label-dark: #111111;
  }

  html, body {
    margin: 0;
    padding: 0;
    overflow: hidden;
    background: var(--sky-deep);
  }

  .canvas {
    width: 1200px;
    height: 848px;
    position: relative;
    overflow: hidden;
  }

  .canvas svg {
    display: block;
    width: 1200px;
    height: 848px;
  }

  .principle-label {
    font-family: "Jost", "Futura", sans-serif;
    font-weight: 800;
    fill: var(--label-light);
    letter-spacing: 0.3px;
  }

  .core-label {
    font-family: "Jost", "Futura", sans-serif;
    font-weight: 700;
    fill: var(--label-dark);
    font-size: 19px;
  }

  .stop-sky-light { stop-color: var(--sky-light); }
  .stop-sky-mid { stop-color: var(--sky-mid); }
  .stop-sky-deep { stop-color: var(--sky-deep); }
  .stop-value-light { stop-color: var(--value-light); }
  .stop-value-dark { stop-color: var(--value-dark); }
  .stop-models-light { stop-color: var(--models-light); }
  .stop-models-dark { stop-color: var(--models-dark); }
  .stop-entropy-light { stop-color: var(--entropy-light); }
  .stop-entropy-dark { stop-color: var(--entropy-dark); }
  .stop-teaming-light { stop-color: var(--teaming-light); }
  .stop-teaming-dark { stop-color: var(--teaming-dark); }
  .stop-core-light { stop-color: var(--core-light); }
  .stop-core-dark { stop-color: var(--core-dark); }

  .grid-stroke { stroke: var(--grid-line); }
  .hub-disc { fill: var(--hub-glow); }

  .segment { stroke-width: 3; stroke-linejoin: round; }
  .segment-value { fill: url(#fill-value); stroke: var(--value-rim); }
  .segment-models { fill: url(#fill-models); stroke: var(--models-rim); }
  .segment-entropy { fill: url(#fill-entropy); stroke: var(--entropy-rim); }
  .segment-teaming { fill: url(#fill-teaming); stroke: var(--teaming-rim); }

  .core-circle { fill: url(#fill-core); stroke: var(--core-rim); stroke-width: 3; }
</style>
</head>
<body>
<main class="canvas">
  <svg viewBox="0 0 842 595" xmlns="http://www.w3.org/2000/svg">
    <defs>
      <radialGradient id="fill-sky" cx="50%" cy="50%" r="65%">
        <stop offset="0" class="stop-sky-light"/>
        <stop offset="0.5" class="stop-sky-mid"/>
        <stop offset="1" class="stop-sky-deep"/>
      </radialGradient>

      <pattern id="blueprint-grid" width="42" height="42" patternUnits="userSpaceOnUse" x="10" y="12">
        <path d="M 42 0 L 0 0 0 42" fill="none" class="grid-stroke" stroke-width="1.4"/>
      </pattern>

      <pattern id="hub-grid" width="21" height="21" patternUnits="userSpaceOnUse" x="10" y="12">
        <path d="M 21 0 L 0 0 0 21" fill="none" class="grid-stroke" stroke-width="1"/>
      </pattern>

      <linearGradient id="fill-value" x1="0" y1="0" x2="1" y2="0">
        <stop offset="0" class="stop-value-light"/>
        <stop offset="1" class="stop-value-dark"/>
      </linearGradient>
      <linearGradient id="fill-models" x1="0" y1="0" x2="1" y2="0">
        <stop offset="0" class="stop-models-light"/>
        <stop offset="1" class="stop-models-dark"/>
      </linearGradient>
      <linearGradient id="fill-entropy" x1="1" y1="0" x2="0" y2="0">
        <stop offset="0" class="stop-entropy-light"/>
        <stop offset="1" class="stop-entropy-dark"/>
      </linearGradient>
      <linearGradient id="fill-teaming" x1="1" y1="0" x2="0" y2="0">
        <stop offset="0" class="stop-teaming-light"/>
        <stop offset="1" class="stop-teaming-dark"/>
      </linearGradient>
      <linearGradient id="fill-core" x1="0" y1="0" x2="1" y2="0">
        <stop offset="0" class="stop-core-light"/>
        <stop offset="1" class="stop-core-dark"/>
      </linearGradient>

      <!-- ring segment, pointing up, centred on the hub -->
      <path id="ring-segment"
            d="M -142.7 -170.1 A 222 222 0 0 1 142.7 -170.1
               L 66.9 -79.7 A 104 104 0 0 0 10.9 -103.4
               L 0 -90 L -10.9 -103.4 A 104 104 0 0 0 -66.9 -79.7 Z"/>

      <!-- label tracks, clockwise arcs -->
      <path id="track-outer" d="M -176 0 A 176 176 0 0 1 176 0"/>
      <path id="track-inner" d="M -148 0 A 148 148 0 0 1 148 0"/>
      <path id="track-bottom" d="M -170 0 A 170 170 0 0 0 170 0"/>
    </defs>

    <!-- background -->
    <rect class="backdrop" width="842" height="595" fill="url(#fill-sky)"/>
    <rect class="backdrop-grid" width="842" height="595" fill="url(#blueprint-grid)"/>

    <g class="diagram" transform="translate(421 297)">
      <!-- hub glow behind centre -->
      <circle class="hub-disc" r="106"/>
      <circle r="106" fill="url(#hub-grid)"/>

      <!-- Fulfil Customer Value -->
      <g class="principle principle-value">
        <use href="#ring-segment" class="segment segment-value"/>
        <text class="principle-label" font-size="22">
          <textPath href="#track-outer" startOffset="50%" text-anchor="middle">Fulfil Customer</textPath>
        </text>
        <text class="principle-label" font-size="22">
          <textPath href="#track-inner" startOffset="50%" text-anchor="middle">Value</textPath>
        </text>
      </g>

      <!-- Build Shared Models -->
      <g class="principle principle-models" transform="rotate(90)">
        <use href="#ring-segment" class="segment segment-models"/>
        <text class="principle-label" font-size="24">
          <textPath href="#track-outer" startOffset="50%" text-anchor="middle">Build Shared</textPath>
        </text>
        <text class="principle-label" font-size="21">
          <textPath href="#track-inner" startOffset="50%" text-anchor="middle">Models</textPath>
        </text>
      </g>

      <!-- Suppress Entropy -->
      <g class="principle principle-entropy">
        <use href="#ring-segment" class="segment segment-entropy" transform="rotate(180)"/>
        <text class="principle-label" font-size="21" dy="-2">
          <textPath href="#track-bottom" startOffset="50%" text-anchor="middle">Suppress Entropy</textPath>
        </text>
      </g>

      <!-- Eliminate Teaming Threats -->
      <g class="principle principle-teaming" transform="rotate(-90)">
        <use href="#ring-segment" class="segment segment-teaming"/>
        <text class="principle-label" font-size="22">
          <textPath href="#track-outer" startOffset="50%" text-anchor="middle">Eliminate Teaming</textPath>
        </text>
        <text class="principle-label" font-size="22">
          <textPath href="#track-inner" startOffset="50%" text-anchor="middle">Threats</textPath>
        </text>
      </g>

      <!-- centre goal -->
      <g class="core">
        <circle class="core-circle" r="72"/>
        <text class="core-label" text-anchor="middle" y="-5">Achieve</text>
        <text class="core-label" text-anchor="middle" y="18">Outcomes</text>
      </g>
    </g>
  </svg>
</main>
</body>
</html>
```